Varnell Solvex Business Card Design

We are looking to make our business cards consistent and modernize them. They are very boring and want to add color.
The final design should communicate a business feel and we are focused on our customer.

Industry/Entity Type

Business

Contact Information for Business Card

Varnell Solvex Corporation
812 W. Harlow Avenue
Suite 342
Itasca, IL 60871
Renata Obrovski
Marketing Manager
robrovski@varnellsolvex.example
630-555-0148
The Customer Centered Specialty Chemical Distributor

Requirements
Must have
• 400 lb stock
Common font
Both sides but don't fill whole back side
Nice to have
• Metallic finish, raised print or spot gloss
Should not have
• cheap paper

```html
<!DOCTYPE html>
<html lang="en">
<head>
<meta charset="UTF-8">
<title>Varnell Solvex Business Card Design</title>
<link rel="stylesheet" href="https://fonts.googleapis.com/css2?family=Caladea:wght@400;700&family=Carlito&family=Open+Sans:wght@400&display=swap">
<style>
  :root {
    --brand-green: #0f5a3f;
    --card-white: #ffffff;
    --text-dark: #2b2b2b;
    --backdrop: #3b3b3b;
  }
  * { margin: 0; padding: 0; box-sizing: border-box; }
  html, body { width: 1200px; height: 481px; overflow: hidden; }
  body { background: var(--backdrop); position: relative; }

  .card {
    position: absolute;
    top: 92px;
    width: 520px;
    height: 296px;
    background: var(--card-white);
    border-radius: 14px;
    overflow: hidden;
  }
  .card--front { left: 76px; }
  .card--back { left: 626px; width: 514px; }

  .brand-panel {
    position: absolute; left: 0; top: 0;
    width: 168px; height: 210px;
    background: var(--brand-green);
    color: var(--card-white);
    font-family: "Carlito", sans-serif;
    font-size: 23px;
    line-height: 31px;
    text-align: center;
    padding-top: 118px;
  }
  .brand-panel__mark {
    position: absolute; left: 50%; top: 34px;
    width: 44px; height: 44px;
    margin-left: -22px;
    background: var(--card-white);
  }

  .holder {
    position: absolute; right: 26px; top: 18px;
    text-align: right;
    font-family: "Caladea", serif;
    color: var(--brand-green);
  }
  .holder__name { font-size: 21px; line-height: 26px; }
  .holder__title { font-size: 15px; margin-top: 10px; }

  .contact {
    position: absolute; left: 250px; top: 146px;
    list-style: none;
    font-family: "Open Sans", sans-serif;
    font-size: 14.5px;
    color: var(--text-dark);
  }
  .contact__item { position: relative; padding-left: 28px; line-height: 20px; margin-bottom: 12px; }
  .contact__item svg { position: absolute; left: 4px; top: 2px; fill: var(--brand-green); }

  .back-brand {
    position: absolute; left: 0; right: 0; top: 52px;
    text-align: center;
  }
  .back-brand__mark {
    display: block; margin: 0 auto 34px;
    width: 44px; height: 44px;
    background: var(--brand-green);
  }
  .back-brand__name {
    font-family: "Caladea", serif;
    font-weight: 700;
    font-size: 31px;
    color: var(--brand-green);
  }

  .stock-tag {
    position: absolute; right: 0; top: 232px;
    width: 140px; height: 30px;
    background: var(--brand-green);
    border-radius: 15px 0 0 15px;
    color: var(--card-white);
    font-family: "Open Sans", sans-serif;
    font-size: 17px;
    line-height: 30px;
    text-align: center;
  }
</style>
</head>
<body>
  <section class="card card--front">
    <div class="brand-panel">
      <span class="brand-panel__mark"></span>
      Varnell Solvex<br>Corporation
    </div>
    <div class="holder">
      <p class="holder__name">Renata Obrovski</p>
      <p class="holder__title">Marketing Manager</p>
    </div>
    <ul class="contact">
      <li class="contact__item">
        <svg width="14" height="18" viewBox="0 0 14 18"><path d="M7 0C3.1 0 0 3.1 0 7c0 5 7 11 7 11s7-6 7-11c0-3.9-3.1-7-7-7zm0 9.5A2.5 2.5 0 1 1 7 4.5a2.5 2.5 0 0 1 0 5z"/></svg>
        812 W. Harlow Avenue Suite<br>342 Itasca, IL 60871
      </li>
      <li class="contact__item">
        <svg width="16" height="16" viewBox="0 0 24 24"><path d="M6.6 10.8a15.1 15.1 0 0 0 6.6 6.6l2.2-2.2c.3-.3.7-.4 1-.2 1.1.4 2.3.6 3.6.6.6 0 1 .4 1 1V20c0 .6-.4 1-1 1A17 17 0 0 1 3 4c0-.6.4-1 1-1h3.5c.6 0 1 .4 1 1 0 1.3.2 2.5.6 3.6.1.3 0 .7-.2 1z"/></svg>
        630-555-0148
      </li>
      <li class="contact__item">
        <svg width="17" height="14" viewBox="0 0 17 14" style="top:4px"><path d="M0 0h17v2L8.5 7 0 2z"/><path d="M0 4l8.5 5L17 4v10H0z"/></svg>
        robrovski@varnellsolvex.example
      </li>
    </ul>
  </section>

  <section class="card card--back">
    <div class="back-brand">
      <span class="back-brand__mark"></span>
      <p class="back-brand__name">Varnell Solvex Corporation</p>
    </div>
    <div class="stock-tag">400 lb stock</div>
  </section>
</body>
</html>
```